Mediation service showing compassion, collaboration, and resolution

I would like to purchase a customized version of a design you have previously submitted - https://www.pixelbidhub.com/design/48172635

Hello,

I would like a design for a flyer for my mediation business.
I also want to include a message that says that I offer rates on sliding scale.
My website is: www.morvantelkresolve.com

Let me know what other details you might want?

Thank you,

Teodric

Target Market(s)

Local community, western Massachusetts USA. Businesses, families, individuals.

Industry/Entity Type

Mediation, Legal, Alternative Dispute Resolution, Divorce, Unions

Font styles to use
Sans Serif

Colors
0094D4
00A9DD
6FCCEA
C7EBF8
E9F6FB
00AB8E
00BBA5
67D7C9
C6EFE9
E9F9F6

Requirements
Must have
• “Sliding scale rates available “. Phone and email details. +1.555.384.7290 and email: teodric@morvantelkresolve.com as well as we code to my website www.morvantelkresolve.com

```html
<!DOCTYPE html>
<html lang="en">
<head>
<meta charset="utf-8">
<title>Mediation Flyer – Teodric Morvantelk</title>
<link rel="stylesheet" href="https://fonts.googleapis.com/css2?family=Libre+Baskerville:wght@400;700&family=Montserrat:wght@400;600;700&display=swap">
<style>
  :root {
    --teal-dark: #336c7d;
    --teal-mid: #3b8b9a;
    --blue-accent: #1d8fc4;
    --box-light: #e6f0f4;
    --text-dark: #2a3a44;
    --text-body: #4a5862;
    --stage-grey: #d6d6d6;
    --white: #ffffff;
  }
  * { margin: 0; padding: 0; box-sizing: border-box; }
  html, body { width: 1200px; height: 3148px; overflow: hidden; background: var(--white); }
  .canvas { position: relative; width: 1200px; height: 3148px; }
  .stage-top { position: absolute; left: 0; top: 0; width: 1200px; height: 1420px; background: var(--stage-grey); }
  .slot { position: absolute; width: 1160px; height: 1688px; transform-origin: 0 0; }
  .slot-top { left: 150px; top: 55px; transform: scale(0.776); }
  .slot-bottom { left: 20px; top: 1460px; }

  .flyer { position: relative; width: 1160px; height: 1688px; background: var(--white); overflow: hidden;
    font-family: "Montserrat", Arial, sans-serif; color: var(--text-body); }
  .texture { position: absolute; left: 0; top: 0; width: 760px; height: 420px;
    background: radial-gradient(ellipse at 20% 10%, #eef4f6 0%, rgba(255,255,255,0) 70%); }
  .brand { position: absolute; left: 100px; top: 40px; width: 420px; text-align: center; }
  .brand-name { font-family: "Libre Baskerville", Georgia, serif; font-size: 34px; color: var(--text-dark); }
  .brand-tag { font-size: 15px; font-weight: 600; color: var(--text-dark); margin-top: 8px; letter-spacing: 0.5px; }

  .shape-layer { position: absolute; left: 0; top: 0; width: 1160px; height: 1688px; }
  .hero-photo { position: absolute; left: 680px; top: -20px; width: 520px; height: 520px; border-radius: 50%;
    border: 22px solid var(--teal-mid);
    background: radial-gradient(circle at 45% 55%, #c9b8a4 0%, #7e8d99 35%, #3f5e72 70%, #25404f 100%); }

  .headline { position: absolute; left: 70px; top: 175px; width: 620px;
    font-family: "Libre Baskerville", Georgia, serif; font-weight: 700; font-size: 54px; line-height: 1.12;
    color: var(--white); text-transform: uppercase; }

  .about { position: absolute; left: 100px; top: 400px; width: 520px; }
  .about-title { font-family: "Libre Baskerville", Georgia, serif; font-size: 38px; color: var(--text-dark); margin-bottom: 14px; }
  .about-title span { color: var(--blue-accent); }
  .about p { font-size: 15px; line-height: 1.45; margin-bottom: 12px; }

  .rates { position: absolute; left: 620px; top: 520px; width: 520px; padding: 18px 0 20px 50px;
    border: 4px solid var(--teal-mid); border-right: none; color: var(--text-dark); }
  .rates-small { font-size: 34px; font-weight: 600; letter-spacing: 1px; }
  .rates-big { font-size: 66px; font-weight: 700; line-height: 1; margin-top: 6px; }
  .rates-sub { font-size: 34px; font-weight: 700; color: var(--teal-mid); margin-top: 4px; }

  .portrait { position: absolute; left: 800px; top: 740px; width: 240px; height: 240px; border-radius: 50%;
    border: 10px solid var(--teal-mid);
    background: radial-gradient(circle at 50% 45%, #d7a989 0%, #b98466 40%, #7a8d9d 75%, #5b7485 100%); }
  .bio { position: absolute; left: 630px; top: 1000px; width: 500px; }
  .bio-name { font-family: "Libre Baskerville", Georgia, serif; font-size: 40px; color: var(--text-dark); text-align: center; margin-bottom: 18px; }
  .bio p { font-size: 17px; line-height: 1.5; }

  .services-head { position: absolute; left: 0; top: 740px; width: 590px; height: 78px; background: var(--teal-dark);
    border-radius: 0 40px 0 0; }
  .services-head h2 { font-family: "Libre Baskerville", Georgia, serif; font-weight: 400; font-size: 40px; color: var(--white);
    line-height: 78px; padding-left: 90px; }
  .services-box { position: absolute; left: 60px; top: 818px; width: 520px; height: 720px; background: var(--box-light);
    padding: 26px 20px 20px 36px; }
  .services-list { list-style: none; }
  .services-list li { display: flex; align-items: flex-start; gap: 14px; font-size: 18px; font-weight: 700;
    color: var(--text-dark); line-height: 1.3; margin-bottom: 20px; }
  .services-list svg { flex: 0 0 24px; margin-top: 1px; }

  .footer { position: absolute; left: 0; bottom: 14px; width: 1160px; display: flex; justify-content: center;
    align-items: center; gap: 34px; color: var(--white); }
  .footer-url { font-size: 24px; font-weight: 600; letter-spacing: 3px; }
  .footer-contact { font-size: 17px; font-weight: 600; display: flex; align-items: center; gap: 8px; }
</style>
</head>
<body>
<div class="canvas">
  <div class="stage-top"></div>

  <div class="slot slot-top">
    <div class="flyer">
      <div class="texture"></div>
      <svg class="shape-layer" viewBox="0 0 1160 1688" aria-hidden="true">
        <path d="M0 150 H640 Q760 150 760 260 Q760 370 640 370 H0 Z" fill="#336c7d"/>
        <path d="M0 1630 Q300 1550 620 1590 Q900 1620 1160 1570 V1688 H0 Z" fill="#336c7d"/>
        <path d="M0 1605 Q300 1530 620 1570 Q900 1600 1160 1550" fill="none" stroke="#3b8b9a" stroke-width="6"/>
        <path d="M20 830 V1540" stroke="#3b8b9a" stroke-width="5"/>
      </svg>
      <div class="brand"><div class="brand-name">Teodric T Morvantelk</div><div class="brand-tag">Alternative Dispute Resolution</div></div>
      <div class="hero-photo" role="img" aria-label="Photo of two people shaking hands"></div>
      <h1 class="headline">Mediation is the way to happiness</h1>
      <section class="about">
        <h2 class="about-title">What is <span>Mediation?</span></h2>
        <p>Mediation is a form of facilitated negotiation, by a mediator, who helps the parties engage in a dialog to search for a joint agreement. All decisions, from agreeing to participate in the mediation, to possible terms of an agreement, are decided by the parties.</p>
        <p>The mediator has no authority over the parties nor imposes any directives. The mediator is there to help the parties find their interests, list and organize the options they have or the alternatives and the outcome probabilities for each outcome a resolution via the mediation process.</p>
      </section>
      <div class="rates"><div class="rates-small">WE OFFER</div><div class="rates-big">RATES ON</div><div class="rates-sub">SLIDING SCALE</div></div>
      <div class="services-head"><h2>Services Provided</h2></div>
      <div class="services-box">
        <ul class="services-list">
          <li><svg width="24" height="24" viewBox="0 0 24 24"><circle cx="12" cy="12" r="11" fill="#336c7d"/><path d="M7 12.5l3.2 3.2L17 9" fill="none" stroke="#fff" stroke-width="2.4"/></svg>Divorce and Family Mediation (Sliding scale rates)</li>
          <li><svg width="24" height="24" viewBox="0 0 24 24"><circle cx="12" cy="12" r="11" fill="#336c7d"/><path d="M7 12.5l3.2 3.2L17 9" fill="none" stroke="#fff" stroke-width="2.4"/></svg>Commercial and business related Mediation</li>
          <li><svg width="24" height="24" viewBox="0 0 24 24"><circle cx="12" cy="12" r="11" fill="#336c7d"/><path d="M7 12.5l3.2 3.2L17 9" fill="none" stroke="#fff" stroke-width="2.4"/></svg>International business and trading conflict mediation</li>
          <li><svg width="24" height="24" viewBox="0 0 24 24"><circle cx="12" cy="12" r="11" fill="#336c7d"/><path d="M7 12.5l3.2 3.2L17 9" fill="none" stroke="#fff" stroke-width="2.4"/></svg>Merger Negotiations &amp; Business Collaboration</li>
          <li><svg width="24" height="24" viewBox="0 0 24 24"><circle cx="12" cy="12" r="11" fill="#336c7d"/><path d="M7 12.5l3.2 3.2L17 9" fill="none" stroke="#fff" stroke-width="2.4"/></svg>Mediation between dealer, agent, distributor and supplier, manufacturer</li>
          <li><svg width="24" height="24" viewBox="0 0 24 24"><circle cx="12" cy="12" r="11" fill="#336c7d"/><path d="M7 12.5l3.2 3.2L17 9" fill="none" stroke="#fff" stroke-width="2.4"/></svg>Contract negotiation consultancy</li>
          <li><svg width="24" height="24" viewBox="0 0 24 24"><circle cx="12" cy="12" r="11" fill="#336c7d"/><path d="M7 12.5l3.2 3.2L17 9" fill="none" stroke="#fff" stroke-width="2.4"/></svg>Employment contract negotiations</li>
          <li><svg width="24" height="24" viewBox="0 0 24 24"><circle cx="12" cy="12" r="11" fill="#336c7d"/><path d="M7 12.5l3.2 3.2L17 9" fill="none" stroke="#fff" stroke-width="2.4"/></svg>Mediation for property or entity division</li>
          <li><svg width="24" height="24" viewBox="0 0 24 24"><circle cx="12" cy="12" r="11" fill="#336c7d"/><path d="M7 12.5l3.2 3.2L17 9" fill="none" stroke="#fff" stroke-width="2.4"/></svg>Workplace Mediation</li>
          <li><svg width="24" height="24" viewBox="0 0 24 24"><circle cx="12" cy="12" r="11" fill="#336c7d"/><path d="M7 12.5l3.2 3.2L17 9" fill="none" stroke="#fff" stroke-width="2.4"/></svg>Mediation Coaching</li>
          <li><svg width="24" height="24" viewBox="0 0 24 24"><circle cx="12" cy="12" r="11" fill="#336c7d"/><path d="M7 12.5l3.2 3.2L17 9" fill="none" stroke="#fff" stroke-width="2.4"/></svg>Ombuds contracting</li>
          <li><svg width="24" height="24" viewBox="0 0 24 24"><circle cx="12" cy="12" r="11" fill="#336c7d"/><path d="M7 12.5l3.2 3.2L17 9" fill="none" stroke="#fff" stroke-width="2.4"/></svg>Mediation via videoconference</li>
          <li><svg width="24" height="24" viewBox="0 0 24 24"><circle cx="12" cy="12" r="11" fill="#336c7d"/><path d="M7 12.5l3.2 3.2L17 9" fill="none" stroke="#fff" stroke-width="2.4"/></svg>Meetings Facilitations</li>
        </ul>
      </div>
      <div class="portrait" role="img" aria-label="Portrait photo of the mediator"></div>
      <section class="bio">
        <h2 class="bio-name">Teodric Morvantelk</h2>
        <p>Working in the international business world for over 30 years, Teodric has become very skilled in negotiation, mediation, and resolution of conflicts with his clients and his suppliers. By necessity, he managed conflicts between managers and workers. He also became skilled at negotiating terms and relationships between companies and their representatives, as well as within companies. Over the course of his career, Teodric has had at least 400 employees reporting to him, in which many occasions, he acted as an ombudsman, helping to reach agreements between employees during times of conflict.</p>
      </section>
      <div class="footer">
        <div class="footer-contact"><svg width="18" height="18" viewBox="0 0 24 24"><path d="M6.6 10.8a15 15 0 0 0 6.6 6.6l2.2-2.2a1 1 0 0 1 1-.25 11.4 11.4 0 0 0 3.6.57 1 1 0 0 1 1 1V20a1 1 0 0 1-1 1A17 17 0 0 1 3 4a1 1 0 0 1 1-1h3.5a1 1 0 0 1 1 1c0 1.25.2 2.45.57 3.57a1 1 0 0 1-.25 1z" fill="#fff"/></svg>+1.555.384.7290</div>
        <div class="footer-url">www.morvantelkresolve.com</div>
        <div class="footer-contact"><svg width="18" height="18" viewBox="0 0 24 24"><rect x="2" y="5" width="20" height="14" rx="2" fill="none" stroke="#fff" stroke-width="2"/><path d="M3 6l9 7 9-7" fill="none" stroke="#fff" stroke-width="2"/></svg>teodric@morvantelkresolve.com</div>
      </div>
    </div>
  </div>

  <div class="slot slot-bottom">
    <div class="flyer">
      <div class="texture"></div>
      <svg class="shape-layer" viewBox="0 0 1160 1688" aria-hidden="true">
        <path d="M0 150 H640 Q760 150 760 260 Q760 370 640 370 H0 Z" fill="#336c7d"/>
        <path d="M0 1630 Q300 1550 620 1590 Q900 1620 1160 1570 V1688 H0 Z" fill="#336c7d"/>
        <path d="M0 1605 Q300 1530 620 1570 Q900 1600 1160 1550" fill="none" stroke="#3b8b9a" stroke-width="6"/>
        <path d="M20 830 V1540" stroke="#3b8b9a" stroke-width="5"/>
      </svg>
      <div class="brand"><div class="brand-name">Teodric T Morvantelk</div><div class="brand-tag">Alternative Dispute Resolution</div></div>
      <div class="hero-photo" role="img" aria-label="Photo of two people shaking hands"></div>
      <h1 class="headline">Mediation is the way to happiness</h1>
      <section class="about">
        <h2 class="about-title">What is <span>Mediation?</span></h2>
        <p>Mediation is a form of facilitated negotiation, by a mediator, who helps the parties engage in a dialog to search for a joint agreement. All decisions, from agreeing to participate in the mediation, to possible terms of an agreement, are decided by the parties.</p>
        <p>The mediator has no authority over the parties nor imposes any directives. The mediator is there to help the parties find their interests, list and organize the options they have or the alternatives and the outcome probabilities for each outcome a resolution via the mediation process.</p>
      </section>
      <div class="rates"><div class="rates-small">WE OFFER</div><div class="rates-big">RATES ON</div><div class="rates-sub">SLIDING SCALE</div></div>
      <div class="services-head"><h2>Services Provided</h2></div>
      <div class="services-box">
        <ul class="services-list">
          <li><svg width="24" height="24" viewBox="0 0 24 24"><circle cx="12" cy="12" r="11" fill="#336c7d"/><path d="M7 12.5l3.2 3.2L17 9" fill="none" stroke="#fff" stroke-width="2.4"/></svg>Divorce and Family Mediation (Sliding scale rates)</li>
          <li><svg width="24" height="24" viewBox="0 0 24 24"><circle cx="12" cy="12" r="11" fill="#336c7d"/><path d="M7 12.5l3.2 3.2L17 9" fill="none" stroke="#fff" stroke-width="2.4"/></svg>Commercial and business related Mediation</li>
          <li><svg width="24" height="24" viewBox="0 0 24 24"><circle cx="12" cy="12" r="11" fill="#336c7d"/><path d="M7 12.5l3.2 3.2L17 9" fill="none" stroke="#fff" stroke-width="2.4"/></svg>International business and trading conflict mediation</li>
          <li><svg width="24" height="24" viewBox="0 0 24 24"><circle cx="12" cy="12" r="11" fill="#336c7d"/><path d="M7 12.5l3.2 3.2L17 9" fill="none" stroke="#fff" stroke-width="2.4"/></svg>Merger Negotiations &amp; Business Collaboration</li>
          <li><svg width="24" height="24" viewBox="0 0 24 24"><circle cx="12" cy="12" r="11" fill="#336c7d"/><path d="M7 12.5l3.2 3.2L17 9" fill="none" stroke="#fff" stroke-width="2.4"/></svg>Mediation between dealer, agent, distributor and supplier, manufacturer</li>
          <li><svg width="24" height="24" viewBox="0 0 24 24"><circle cx="12" cy="12" r="11" fill="#336c7d"/><path d="M7 12.5l3.2 3.2L17 9" fill="none" stroke="#fff" stroke-width="2.4"/></svg>Contract negotiation consultancy</li>
          <li><svg width="24" height="24" viewBox="0 0 24 24"><circle cx="12" cy="12" r="11" fill="#336c7d"/><path d="M7 12.5l3.2 3.2L17 9" fill="none" stroke="#fff" stroke-width="2.4"/></svg>Employment contract negotiations</li>
          <li><svg width="24" height="24" viewBox="0 0 24 24"><circle cx="12" cy="12" r="11" fill="#336c7d"/><path d="M7 12.5l3.2 3.2L17 9" fill="none" stroke="#fff" stroke-width="2.4"/></svg>Mediation for property or entity division</li>
          <li><svg width="24" height="24" viewBox="0 0 24 24"><circle cx="12" cy="12" r="11" fill="#336c7d"/><path d="M7 12.5l3.2 3.2L17 9" fill="none" stroke="#fff" stroke-width="2.4"/></svg>Workplace Mediation</li>
          <li><svg width="24" height="24" viewBox="0 0 24 24"><circle cx="12" cy="12" r="11" fill="#336c7d"/><path d="M7 12.5l3.2 3.2L17 9" fill="none" stroke="#fff" stroke-width="2.4"/></svg>Mediation Coaching</li>
          <li><svg width="24" height="24" viewBox="0 0 24 24"><circle cx="12" cy="12" r="11" fill="#336c7d"/><path d="M7 12.5l3.2 3.2L17 9" fill="none" stroke="#fff" stroke-width="2.4"/></svg>Ombuds contracting</li>
          <li><svg width="24" height="24" viewBox="0 0 24 24"><circle cx="12" cy="12" r="11" fill="#336c7d"/><path d="M7 12.5l3.2 3.2L17 9" fill="none" stroke="#fff" stroke-width="2.4"/></svg>Mediation via videoconference</li>
          <li><svg width="24" height="24" viewBox="0 0 24 24"><circle cx="12" cy="12" r="11" fill="#336c7d"/><path d="M7 12.5l3.2 3.2L17 9" fill="none" stroke="#fff" stroke-width="2.4"/></svg>Meetings Facilitations</li>
        </ul>
      </div>
      <div class="portrait" role="img" aria-label="Portrait photo of the mediator"></div>
      <section class="bio">
        <h2 class="bio-name">Teodric Morvantelk</h2>
        <p>Working in the international business world for over 30 years, Teodric has become very skilled in negotiation, mediation, and resolution of conflicts with his clients and his suppliers. By necessity, he managed conflicts between managers and workers. He also became skilled at negotiating terms and relationships between companies and their representatives, as well as within companies. Over the course of his career, Teodric has had at least 400 employees reporting to him, in which many occasions, he acted as an ombudsman, helping to reach agreements between employees during times of conflict.</p>
      </section>
      <div class="footer">
        <div class="footer-contact"><svg width="18" height="18" viewBox="0 0 24 24"><path d="M6.6 10.8a15 15 0 0 0 6.6 6.6l2.2-2.2a1 1 0 0 1 1-.25 11.4 11.4 0 0 0 3.6.57 1 1 0 0 1 1 1V20a1 1 0 0 1-1 1A17 17 0 0 1 3 4a1 1 0 0 1 1-1h3.5a1 1 0 0 1 1 1c0 1.25.2 2.45.57 3.57a1 1 0 0 1-.25 1z" fill="#fff"/></svg>+1.555.384.7290</div>
        <div class="footer-url">www.morvantelkresolve.com</div>
        <div class="footer-contact"><svg width="18" height="18" viewBox="0 0 24 24"><rect x="2" y="5" width="20" height="14" rx="2" fill="none" stroke="#fff" stroke-width="2"/><path d="M3 6l9 7 9-7" fill="none" stroke="#fff" stroke-width="2"/></svg>teodric@morvantelkresolve.com</div>
      </div>
    </div>
  </div>
</div>
</body>
</html>
```